Real Estate Website

We need a web design for a new site that is focused on real estate listings and information for the Singapore, Malaysian and Australian market.

The web site will have listings of available real estate for sale, past transaction data on real estate, information about neighborhoods where the real estate is located.
Website URL will likely be www.havenlotz.com. We are also open to suggestions on site names (assuming URL is available).

We like the simplicity of a similar US site called Pevondo.com - and want to focus on providing a similar "clean" user interface where users can find the information they need. The final design should be user friendly, be visually compelling with a focus on ease of navigation.

Requirements to have at least 5 web pages designed that will display the data as in the attached document for any given territory. We will need to receive
- HTML/CSS/JavaScript, and all images
- any design icons for common objects (e.g. house/home, map, user, agent, trend chart, contact, bathroom, bedroom, garage, furniture, price, ...etc).
Updates

Hi

I just added more details to the brief and committed to pay for the project.
Please review the additional information and submit your final designs by June 14th (or sooner) as we have a deadline to meet. 

Let me know if you have any questions, I will try to be prompt in my responses. 
Thanks.

Target Market(s)

Consumers who are researching real estate to purchase or sell

Industry/Entity Type

Real Estate

Requirements
Must have
• Data in attached document needs to be displayed.

```html
<!DOCTYPE html>
<html lang="en">
<head>
<meta charset="utf-8">
<title>Co Logo – Real Estate Listings</title>
<link rel="stylesheet" href="https://fonts.googleapis.com/css2?family=Crimson+Pro:wght@600;700&family=Open+Sans:wght@400;600;700&display=swap">
<style>
  :root {
    --page-bg: #f4f4f4;
    --header-bg: #f1eff0;
    --plum: #3d2f3d;
    --nav-text: #ffffff;
    --nav-soft: #b7c3e6;
    --sky: #a8d4e6;
    --frame: #d9e5f2;
    --periwinkle: #aab8dc;
    --periwinkle-text: #eef2fb;
    --navy: #1b2a4a;
    --field: #d8d3d3;
    --field-border: #aa9d97;
    --arrow: #8f8a8a;
    --card: #ffffff;
    --dot: #9fb5de;
  }
  * { box-sizing: border-box; margin: 0; padding: 0; }
  html, body { width: 1200px; height: 938px; overflow: hidden; background: var(--page-bg); }
  body { position: relative; font-family: "Open Sans", sans-serif; color: var(--navy); }
  .abs { position: absolute; }

  .site-header { left: 174px; top: 0; width: 841px; height: 59px; background: var(--header-bg); }
  .brand { left: 4px; top: 10px; font-family: "Crimson Pro", serif; font-weight: 700; font-size: 30px; color: var(--plum); white-space: nowrap; }
  .main-nav { left: 184px; top: 14px; width: 657px; height: 31px; background: var(--plum); display: flex; flex-wrap: nowrap; align-items: center; padding-left: 12px; white-space: nowrap; overflow: hidden; }
  .main-nav a { font-family: "Crimson Pro", serif; font-weight: 700; font-size: 17px; line-height: 1; color: var(--nav-text); text-decoration: none; margin-right: 10px; white-space: nowrap; flex: none; }
  .main-nav a.current { color: #d9e2f7; }
  .main-nav .utility { margin-left: auto; margin-right: 8px; display: flex; gap: 10px; flex: none; }
  .main-nav .utility a { font-family: "Open Sans", sans-serif; font-weight: 400; font-size: 16px; color: var(--nav-soft); margin: 0; }

  .hero { left: 174px; top: 59px; width: 841px; height: 410px; background: var(--sky); }
  .hero-frame { left: 118px; top: 24px; width: 706px; height: 365px; background: var(--frame); border-radius: 6px; }
  .hero-photo { left: 8px; top: 8px; width: 691px; height: 350px; background: linear-gradient(90deg, #eef1f3 0%, #e6e2dc 45%, #dcd1c6 75%, #ece8e4 100%); }
  .slide-dots { left: 707px; top: 352px; display: flex; gap: 4px; }
  .slide-dots span { width: 19px; height: 19px; border-radius: 50%; background: var(--dot); }

  .search-panel { left: 0; top: 113px; width: 592px; height: 226px; background: rgba(236,236,238,.9); box-shadow: 0 2px 4px rgba(0,0,0,.15); }
  .tabs { left: 22px; top: 16px; display: flex; align-items: center; font-size: 17px; color: #2f4360; white-space: nowrap; }
  .tabs span { margin-right: 38px; }
  .tabs .active { background: var(--periwinkle); color: #2f4360; font-weight: 600; padding: 8px 6px; border-radius: 8px; margin-right: 22px; position: relative; }
  .tabs .active::after { content: ""; position: absolute; left: 36px; bottom: -8px; border: 5px solid transparent; border-top: 5px solid var(--periwinkle); border-left: 5px solid var(--periwinkle); }
  .field { height: 56px; background: var(--field); border: 2px solid var(--field-border); font-weight: 700; font-size: 17px; color: var(--navy); padding: 12px 10px; white-space: nowrap; }
  .field.select::after { content: ""; position: absolute; right: 10px; top: 22px; border: 9px solid transparent; border-top: 13px solid var(--arrow); }
  .to-label { font-weight: 700; font-size: 17px; }
  .search-btn { left: 499px; top: 87px; width: 76px; height: 39px; background: var(--plum); border: 3px solid #b8b0ab; border-radius: 2px; }

  .card { top: 480px; width: 260px; height: 289px; background: var(--card); box-shadow: 0 1px 3px rgba(0,0,0,.1); }
  .card-title { left: 0; top: 21px; width: 262px; height: 38px; background: var(--periwinkle); color: var(--periwinkle-text); font-weight: 700; font-size: 18px; padding: 7px 0 0 43px; box-shadow: 0 2px 3px rgba(0,0,0,.15); white-space: nowrap; }
  .photo { left: 26px; top: 59px; }
  .count-row { left: 20px; width: 219px; height: 22px; font-size: 16px; display: flex; align-items: center; padding-left: 16px; border-bottom: 2px dotted #4a4a5a; white-space: nowrap; }
  .count-row b { margin-right: 5px; }
  .count-row .chev { margin-left: auto; margin-right: 6px; font-weight: 700; }
  .count-row.lead { top: 174px; height: 35px; background: var(--periwinkle); color: #fff; border: none; left: 26px; width: 219px; padding-left: 16px; }
  .count-row.lead .chev { color: var(--navy); }
  .agents-label { left: 26px; top: 209px; font-weight: 600; font-size: 16px; }
  .agent-thumb { top: 231px; width: 61px; height: 45px; border: 2px solid #c8c8c8; background: linear-gradient(#e8ecf0, #c9cdd3); }
  .mini-select { top: 217px; height: 21px; background: #c9c6c6; border: 1px solid #a59c98; font-size: 15px; padding: 0 0 0 5px; line-height: 19px; white-space: nowrap; }
  .mini-select::after { content: ""; position: absolute; right: 5px; top: 6px; border: 5px solid transparent; border-top: 7px solid #fff; }
  .card3-label { left: 26px; top: 251px; font-weight: 700; font-size: 15px; color: #2a2a35; white-space: nowrap; }
  .pager { left: 212px; top: 249px; font-weight: 700; font-size: 16px; color: #222; letter-spacing: 10px; }

  .teaser-text { width: 210px; font-size: 12px; line-height: 15.6px; color: var(--navy); }
  .more { font-weight: 700; font-size: 13px; color: #222; }
  .teaser-img { border: 3px solid var(--periwinkle); }

  .footer-bar { left: 174px; top: 893px; width: 841px; height: 16px; background: var(--plum); }
  .footer-nav { left: 200px; top: 915px; width: 778px; display: flex; justify-content: space-between; white-space: nowrap; }
  .footer-nav a { font-family: "Crimson Pro", serif; font-weight: 700; font-size: 12.5px; color: #2a2230; text-decoration: none; text-transform: uppercase; }
</style>
</head>
<body>
  <header class="site-header abs">
    <div class="brand abs">Co Logo</div>
    <nav class="main-nav abs">
      <a class="current" href="#">HOME</a><a href="#">BUY</a><a href="#">RENT</a><a href="#">MORTGAGE</a><a href="#">ADVICE</a><a href="#">LOCAL INFO</a><a href="#">FIND A PRO</a>
      <span class="utility"><a href="#">Log in</a><a href="#">Help</a></span>
    </nav>
  </header>

  <section class="hero abs">
    <div class="hero-frame abs">
      <div class="hero-photo abs" role="img" aria-label="Family relaxing together in a bright living room"></div>
    </div>
    <div class="slide-dots abs"><span></span><span></span><span></span></div>

    <form class="search-panel abs">
      <div class="tabs abs"><span class="active">For Sale</span><span>For Rent</span><span>Sold</span><span>Estimates</span></div>
      <div class="field abs" style="left:16px;top:76px;width:236px;">New York, NY</div>
      <div class="field select abs" style="left:260px;top:76px;width:107px;">Beds</div>
      <div class="field select abs" style="left:375px;top:76px;width:106px;">Baths</div>
      <div class="search-btn abs">
        <svg width="70" height="33" viewBox="0 0 70 33"><circle cx="33" cy="14" r="7" fill="none" stroke="#fff" stroke-width="2.5"/><line x1="38" y1="19" x2="47" y2="26" stroke="#fff" stroke-width="4" stroke-linecap="round"/></svg>
      </div>
      <div class="field abs" style="left:16px;top:153px;width:117px;">$ MIN</div>
      <div class="to-label abs" style="left:136px;top:163px;">To</div>
      <div class="field abs" style="left:157px;top:153px;width:118px;">$ MAX</div>
      <div class="field select abs" style="left:281px;top:153px;width:105px;">Sqft</div>
      <div class="field select abs" style="left:393px;top:153px;width:185px;">Property Type</div>
    </form>
  </section>

  <article class="card abs" style="left:190px;">
    <div class="card-title abs">LOREM IPSUM</div>
    <div class="photo abs" role="img" aria-label="Modern living room with a white sofa" style="width:219px;height:115px;background:linear-gradient(90deg,#d7d3ce,#bdb7b0 60%,#6f6a66);"></div>
    <div class="count-row lead abs"><b>500</b> Lorem Ipsum <span class="chev">›</span></div>
    <div class="count-row abs" style="top:209px;"><b>200</b> Lorem Ipsum <span class="chev">›</span></div>
    <div class="count-row abs" style="top:231px;"><b>150</b> Lorem Ipsum <span class="chev">›</span></div>
    <div class="count-row abs" style="top:251px;"><b>45</b>&nbsp;&nbsp;Lorem Ipsum <span class="chev">›</span></div>
  </article>

  <article class="card abs" style="left:458px;">
    <div class="card-title abs">LOREM IPSUM</div>
    <div class="photo abs" role="img" aria-label="Street map of the neighbourhood with a route" style="width:219px;height:149px;background:linear-gradient(135deg,#e8e4d8,#f0e6b8 50%,#c8d4dc);"></div>
    <div class="agents-label abs">Agents</div>
    <div class="agent-thumb abs" role="img" aria-label="Agent portrait" style="left:27px;"></div>
    <div class="agent-thumb abs" role="img" aria-label="Agent portrait" style="left:108px;"></div>
    <div class="agent-thumb abs" role="img" aria-label="Agent portrait" style="left:184px;"></div>
  </article>

  <article class="card abs" style="left:724px;">
    <div class="card-title abs">LOREM IPSUM</div>
    <div class="photo abs" role="img" aria-label="Open-plan lounge with designer furniture" style="width:220px;height:149px;background:linear-gradient(180deg,#e9e6e0,#cfc6b8 70%,#b9ad9c);"></div>
    <div class="mini-select abs" style="left:26px;width:97px;">All Spaces</div>
    <div class="mini-select abs" style="left:162px;width:97px;">All Styles</div>
    <div class="card3-label abs">LOREM IPSUM</div>
    <div class="pager abs">‹›</div>
  </article>

  <p class="teaser-text abs" style="left:191px;top:785px;">Sed ut perspiciatis unde omnis iste natus error sit voluptatem accusantium doloremque laudantium, totam rem aperiam, eaque ipsa</p>
  <a class="more abs" style="left:260px;top:861px;">more...</a>
  <div class="teaser-img abs" role="img" aria-label="Couple in a bright white dining room" style="left:406px;top:779px;width:148px;height:104px;background:linear-gradient(90deg,#e6e9ec,#c9ced3);"></div>

  <p class="teaser-text abs" style="left:623px;top:785px;">Sed ut perspiciatis unde omnis iste natus error sit voluptatem accusantium doloremque laudantium, totam rem aperiam, eaque ipsa</p>
  <a class="more abs" style="left:692px;top:861px;">more...</a>
  <div class="teaser-img abs" role="img" aria-label="Tablet showing the property app" style="left:839px;top:779px;width:146px;height:104px;background:linear-gradient(180deg,#5a6a7e,#2a3444);"></div>

  <div class="footer-bar abs"></div>
  <nav class="footer-nav abs">
    <a href="#">Home</a><a href="#">Agents</a><a href="#">Submit Listings</a><a href="#">Partners</a><a href="#">Advice</a><a href="#">Privacy</a><a href="#">Careers</a><a href="#">Contact</a><a href="#">Real Estate Apps</a><a href="#">Terms &amp; Conditions</a><a href="#">About</a>
  </nav>
</body>
</html>
```